Elegant Business Cards & Letterhead

We will need the following that need to be designed: Letterhead and Business Cards, there winer will be re-hired for the balance of our stationary needs. Text for the cards and letterheads:

- Corporate Card instead of name
- landline: +971 (4) 632 7140
- mobile: +971 56 3918 065
- 800CARER
- email: dubai@velvet-oaks.example
- www.velvet-oaks.example
- PO Box 387261
Address: Castellan Tower Suite 1706, Dubai UAE

Thank you

Target Market(s)

VIPs, HNWI, High-end Families.

Industry/Entity Type

Luxury Market

Font styles to use
Other font styles liked:
• as explained

Colors

Designer to choose only greyscale colors for use in the design.

Requirements
Must have
• Elegant, Simple, Luxurious, Minimalistic
Nice to have
• Luxury, Golds, Engravings,
Should not have
• Much colors, funky,

```html
<!DOCTYPE html>
<html lang="en">
<head>
<meta charset="utf-8">
<title>Velvet Oaks — Business Cards</title>
<link rel="stylesheet" href="https://fonts.googleapis.com/css2?family=Open+Sans:wght@400;600;700&display=swap">
<style>
  :root {
    --backdrop: #333333;
    --card: #1f1f22;
    --gold: #d9a526;
    --ink-light: #f4f4f4;
  }
  * { margin: 0; padding: 0; box-sizing: border-box; }
  html, body {
    width: 1200px;
    height: 780px;
    overflow: hidden;
    background: var(--backdrop);
    font-family: "Open Sans", Arial, sans-serif;
  }
  .canvas {
    width: 1200px;
    height: 780px;
    display: flex;
    align-items: center;
    justify-content: center;
    gap: 44px;
  }
  .card {
    position: relative;
    width: 540px;
    height: 309px;
    background: var(--card);
    border-bottom: 4px solid var(--gold);
    box-shadow: 0 14px 30px rgba(0, 0, 0, 0.45);
  }
  .brand-name {
    font-weight: 600;
    color: var(--gold);
    text-transform: uppercase;
    letter-spacing: 0.08em;
    white-space: nowrap;
  }

  /* Back of card */
  .card--back {
    display: flex;
    align-items: center;
    justify-content: center;
  }
  .card--back .brand-name { font-size: 44px; }

  /* Front of card */
  .card--front .brand-name {
    position: absolute;
    left: 30px;
    top: 30px;
    font-size: 30px;
  }
  .card-title {
    position: absolute;
    left: 30px;
    top: 168px;
    font-size: 25px;
    font-weight: 700;
    color: var(--gold);
    white-space: nowrap;
  }
  .contact {
    position: absolute;
    left: 30px;
    right: 20px;
    top: 212px;
    font-size: 11.5px;
    line-height: 1.6;
    color: var(--ink-light);
  }
  .contact-row {
    display: flex;
    gap: 18px;
    white-space: nowrap;
  }
  .contact-label {
    color: var(--gold);
    font-weight: 600;
    margin-right: 3px;
  }
  .contact-address {
    white-space: nowrap;
  }
</style>
</head>
<body>
  <main class="canvas">
    <section class="card card--back" aria-label="Business card back">
      <span class="brand-name">Velvet Oaks</span>
    </section>

    <section class="card card--front" aria-label="Business card front">
      <span class="brand-name">Velvet Oaks</span>

      <h1 class="card-title">Corporate Card</h1>

      <div class="contact">
        <div class="contact-row">
          <span><span class="contact-label">T:</span>+971 (4) 632 7140</span>
          <span><span class="contact-label">E:</span>dubai@velvet-oaks.example</span>
          <span><span class="contact-label">W:</span>www.velvet-oaks.example</span>
        </div>
        <div class="contact-row">
          <span><span class="contact-label">M:</span>+971 56 3918 065</span>
          <span><span class="contact-label">Toll free:</span>800CARER</span>
        </div>
        <p class="contact-address">PO Box 387261, Castellan Tower Suite 1706, Dubai UAE</p>
      </div>
    </section>
  </main>
</body>
</html>
```